Wine label refresh

We are wanting to modify our Corran Estate label to include a picture on it.
I have attached the pictures below which we would like on the label. They are of the Corran Estate vineyard. I have also attached an example of another label with a picture on it that we like the style of.
Industry/Entity Type
Vineyard
Requirements
Must have
- The Corran Estate text must stay the same but can be moved down. It still needs to be the same size though.
Marlborough Sauvignon Blanc should remain in the same font and roughly the same size.
Wine of New Zealand also must stay but could potentially be moved.
Nice to have
- It would be nice if we could keep the KL logo on the front label but feel free to experiment with where this goes.

```html
<!DOCTYPE html>
<html lang="en">
<head>
<meta charset="utf-8">
<title>Corran Estate – Marlborough Sauvignon Blanc label</title>
<link rel="stylesheet" href="https://fonts.googleapis.com/css2?family=Cinzel:wght@400&family=Great+Vibes&family=Montserrat:wght@400&display=swap">
<style>
  :root {
    --backdrop: #f2f2f2;
    --label-border: #e9e9ea;
    --label-border-edge: #c9c9cb;
    --panel-top: #2a2a2c;
    --panel-bottom: #8a8b8e;
    --gold: #c9a25a;
    --gold-light: #e3c78a;
    --gold-dark: #a67f3d;
    --script-ink: #3a2a12;
    --small-ink: #8d8d8d;
    --sky: #d9dde0;
    --trees: #3d5a2e;
    --vines: #5f8a3c;
  }
  * { box-sizing: border-box; margin: 0; padding: 0; }
  html, body {
    width: 750px;
    height: 1200px;
    overflow: hidden;
    background: var(--backdrop);
  }
  .canvas {
    position: relative;
    width: 750px;
    height: 1200px;
  }
  .wine-label {
    position: absolute;
    left: 75px;
    top: 235px;
    width: 600px;
    height: 730px;
    background: linear-gradient(90deg, var(--label-border-edge), var(--label-border) 8%, #fafafa 50%, var(--label-border) 92%, var(--label-border-edge));
    padding: 20px 20px 0;
  }
  .label-panel {
    position: relative;
    height: 580px;
    background: linear-gradient(180deg, var(--panel-top) 0%, #4a4a4d 35%, var(--panel-bottom) 62%);
    text-align: center;
    overflow: hidden;
  }
  .monogram {
    position: absolute;
    top: 62px;
    left: 0;
    right: 0;
    font-family: 'Cinzel', serif;
    font-size: 58px;
    color: var(--gold);
    letter-spacing: 2px;
    line-height: 1;
  }
  .estate-name {
    position: absolute;
    top: 188px;
    left: 0;
    right: 0;
    font-family: 'Cinzel', serif;
    font-size: 50px;
    color: var(--gold);
    letter-spacing: 1px;
    line-height: 1;
  }
  .vintage {
    position: absolute;
    top: 258px;
    left: 0;
    right: 0;
    display: flex;
    justify-content: center;
    align-items: center;
    gap: 14px;
    font-family: 'Cinzel', serif;
    font-size: 26px;
    color: var(--gold-light);
  }
  .vintage::before, .vintage::after {
    content: "";
    width: 110px;
    height: 1px;
    background: var(--gold);
  }
  .vineyard-photo {
    position: absolute;
    left: 0;
    right: 0;
    top: 330px;
    height: 250px;
    background: linear-gradient(180deg, var(--sky) 0%, #b9c2c4 22%, var(--trees) 40%, #4b6d34 55%, var(--vines) 100%);
  }
  .varietal-band {
    position: absolute;
    left: 15px;
    right: 15px;
    top: 483px;
    height: 80px;
    background: linear-gradient(90deg, var(--gold-dark), var(--gold-light) 45%, var(--gold) 100%);
    border-top: 2px solid var(--gold-light);
    border-bottom: 2px solid var(--gold-dark);
    display: flex;
    align-items: center;
    justify-content: center;
    font-family: 'Great Vibes', cursive;
    font-size: 44px;
    color: var(--script-ink);
  }
  .label-footer {
    display: flex;
    justify-content: space-between;
    align-items: center;
    padding: 28px 2px 0;
    font-family: 'Montserrat', sans-serif;
    font-size: 17px;
    color: var(--small-ink);
    letter-spacing: 0.5px;
  }
  .footer-rule {
    margin-top: 22px;
    height: 4px;
    background: linear-gradient(90deg, var(--gold-dark), var(--gold-light), var(--gold-dark));
  }
</style>
</head>
<body>
<main class="canvas">
  <section class="wine-label">
    <div class="label-panel">
      <div class="monogram">KL</div>
      <h1 class="estate-name">CORRAN ESTATE</h1>
      <div class="vintage">2012</div>
      <div class="vineyard-photo" role="img" aria-label="Photograph of the Corran Estate vineyard: rows of green vines leading to a line of palm trees and the homestead under a pale sky"></div>
      <div class="varietal-band">Marlborough Sauvignon Blanc</div>
    </div>
    <div class="label-footer">
      <span class="volume">750ml</span>
      <span class="origin">NEW ZEALAND WINE</span>
      <span class="strength">13% alc/vol</span>
    </div>
    <div class="footer-rule"></div>
  </section>
</main>
</body>
</html>
```